Solar panel cleaning flyer design.

I'm looking for a flyer design for my new company called Brightfield Panel Works. We are a South Australian company that professionally clean residential and commercial solar panels. We generate leads by going door to door and need a flyer to hand out to our customers if they are interested in our service. As we are a new company we don't have anything particular in mind so be creative! Must include the company name and logo.

```html
<!DOCTYPE html>
<html lang="en">
<head>
<meta charset="UTF-8">
<title>Brightfield Panel Works – Solar Panel Cleaning Flyer</title>
<link rel="stylesheet" href="https://fonts.googleapis.com/css2?family=Roboto+Condensed:wght@400;700&display=swap">
<style>
  :root{
    --sky-top:#3f86d6;
    --sky-mid:#8fc1ee;
    --sky-haze:#e3eff9;
    --panel-glare:#8fb0e6;
    --panel-light:#3d63b4;
    --panel-mid:#22479a;
    --panel-dark:#0d2866;
    --brand-blue:#1c4fa0;
    --brand-green:#8dc63f;
    --band-green:#9cc83a;
    --footer-fade:rgba(10,28,70,0);
    --footer-navy:rgba(10,28,70,0.85);
    --white:#ffffff;
  }
  *{margin:0;padding:0;box-sizing:border-box;}
  html,body{width:851px;height:1200px;overflow:hidden;background:#fff;}
  .flyer{
    position:relative;width:851px;height:1200px;overflow:hidden;
    font-family:"Roboto Condensed",sans-serif;
  }
  .hero-photo{position:absolute;inset:0;}
  .hero-sky{
    position:absolute;inset:0;
    background:linear-gradient(180deg,
      var(--sky-top) 0%,
      var(--sky-mid) 24%,
      var(--sky-haze) 44%,
      var(--sky-mid) 56%);
  }
  .hero-panels{
    position:absolute;inset:0;
    clip-path:polygon(0 690px,851px 520px,851px 1200px,0 1200px);
    background:
      linear-gradient(115deg,
        var(--panel-light) 0%,
        var(--panel-glare) 30%,
        var(--panel-light) 42%,
        var(--panel-mid) 65%,
        var(--panel-dark) 100%);
  }
  .brand{
    position:absolute;top:58px;right:50px;
    display:flex;flex-direction:column;align-items:flex-end;
  }
  .brand-mark{
    width:96px;height:96px;border-radius:50%;
    background:var(--brand-blue);margin-bottom:12px;margin-right:90px;
  }
  .brand-name{
    font-weight:700;font-size:56px;line-height:1;
    color:var(--brand-blue);text-align:right;
  }
  .headline-band{
    position:absolute;left:0;top:346px;width:766px;height:180px;
    background:var(--band-green);
    padding:10px 20px 0 20px;
  }
  .headline-band p{
    color:var(--white);font-weight:700;font-size:37px;line-height:40px;
    text-transform:uppercase;
  }
  .contact-bar{
    position:absolute;left:0;bottom:0;width:851px;height:150px;
    background:linear-gradient(180deg,var(--footer-fade) 0%,var(--footer-navy) 35%);
    text-align:center;color:var(--white);padding-top:38px;
  }
  .contact-label{font-size:20px;font-weight:700;text-transform:uppercase;line-height:1.1;}
  .contact-phone{font-size:50px;font-weight:400;line-height:1.05;letter-spacing:1px;}
  .contact-web{font-size:22px;color:var(--brand-green);letter-spacing:5px;margin-top:2px;}
</style>
</head>
<body>
<div class="flyer">
  <div class="hero-photo" role="img" aria-label="Bright blue sky with clouds above tilted rows of clean blue solar panels">
    <div class="hero-sky"></div>
    <div class="hero-panels"></div>
  </div>

  <div class="brand">
    <div class="brand-mark"></div>
    <div class="brand-name">Brightfield<br>Panel Works</div>
  </div>

  <div class="headline-band">
    <p>Professional solar panel cleaning<br>for homes and businesses across<br>South Australia. Clean panels make<br>more power – ask us for a quote</p>
  </div>

  <div class="contact-bar">
    <div class="contact-label">For more information call</div>
    <div class="contact-phone">0412 608 351</div>
    <div class="contact-web">www.brightfieldpanels.com.au</div>
  </div>
</div>
</body>
</html>
```